business card for a shoe shop

we would like a business card for a family owned shoe shop.
With this information included.
Darnell's Shoe Store
Family owned since 1947

then on other side
Darnell's Shoe Store
Footwear fitting specialist
Phone: 9187 2630
218 Quarry St, Fernleigh Downs 3187
(cnr. Hartwick Rd and Quarry St)
darnellshoes218@examplemail.com
if could incorporate the purple color on card i have attached.

```html
<!DOCTYPE html>
<html lang="en">
<head>
<meta charset="utf-8">
<title>Darnell's Shoe Store – Business Card</title>
<link href="https://fonts.googleapis.com/css2?family=Amethysta&family=Poppins:ital,wght@1,300&display=swap" rel="stylesheet">
<style>
  :root {
    --purple: #622e8f;
    --ink: #000000;
    --paper: #ffffff;
    --text: #f4f2f7;
    --photo-warm-top: #2a2a3a;
    --photo-warm-bottom: #8a4a26;
    --photo-cool-top: #3a2f3c;
    --photo-cool-bottom: #b08878;
  }
  * { margin: 0; padding: 0; box-sizing: border-box; }
  html, body {
    width: 1200px; height: 1200px; overflow: hidden;
    background: var(--paper);
  }
  .sheet { position: relative; width: 1200px; height: 1200px; }
  .card {
    position: absolute; left: 186px; width: 828px; height: 473px;
    background: var(--purple); overflow: hidden; color: var(--text);
    font-family: "Amethysta", Georgia, serif;
  }
  .card--front { top: 101px; }
  .card--back { top: 625px; }
  .card__blob { position: absolute; inset: 0; width: 100%; height: 100%; }

  .photo { position: absolute; opacity: 0.85; }
  .photo--oxfords {
    left: 0; top: 0; width: 410px; height: 345px;
    background: linear-gradient(180deg, var(--photo-warm-top) 0%, var(--photo-warm-bottom) 100%);
    border-radius: 0 0 48px 0;
  }
  .photo--heels {
    left: 410px; top: 0; width: 418px; height: 325px;
    background: linear-gradient(200deg, var(--photo-cool-bottom) 0%, var(--photo-cool-top) 100%);
    border-radius: 0 0 0 48px;
  }

  .brand {
    font-variant: small-caps; font-weight: 400; letter-spacing: 0.6px;
    font-size: 62px; line-height: 65px;
    -webkit-text-stroke: 0.6px var(--text);
  }
  .card--front .brand {
    position: absolute; left: 400px; width: 390px; top: 131px; text-align: center;
  }
  .tagline {
    position: absolute; left: 400px; width: 390px; top: 285px; text-align: center;
    font-family: "Poppins", Arial, sans-serif; font-style: italic; font-weight: 300;
    font-size: 23px; line-height: 30px;
  }
  .card--back .brand { position: absolute; left: 44px; top: 57px; }
  .specialty {
    position: absolute; left: 44px; top: 198px;
    font-size: 24px; line-height: 28px; letter-spacing: 0.6px;
  }

  .contact {
    position: absolute; top: 334px; list-style: none;
    font-size: 20px; line-height: 40px; letter-spacing: -0.3px; white-space: nowrap;
  }
  .contact--direct { left: 44px; }
  .contact--address { left: 418px; }
  .contact li { display: flex; align-items: center; gap: 14px; }
  .contact .icon { width: 16px; height: 16px; fill: var(--text); flex: none; }
  .contact .indent { padding-left: 30px; }
</style>
</head>
<body>
<main class="sheet">
  <section class="card card--front">
    <svg class="card__blob" viewBox="0 0 828 473" preserveAspectRatio="none" aria-hidden="true">
      <path d="M828 210 C812 330 760 420 560 450 C470 460 432 462 420 473 L828 473 Z" fill="var(--ink)"/>
    </svg>
    <div class="photo photo--oxfords" role="img" aria-label="Photo of feet in dark jeans wearing tan leather lace-up oxford shoes"></div>
    <h1 class="brand">Darnell's<br>Shoe Store</h1>
    <p class="tagline">Family owned since 1947</p>
  </section>

  <section class="card card--back">
    <svg class="card__blob" viewBox="0 0 828 473" preserveAspectRatio="none" aria-hidden="true">
      <path d="M412 0 C416 90 440 160 527 207 C620 255 720 270 828 285 L828 0 Z" fill="var(--ink)"/>
    </svg>
    <div class="photo photo--heels" role="img" aria-label="Photo of legs wearing black pointed high-heel pumps beside a striped skirt"></div>
    <h2 class="brand">Darnell's<br>Shoe Store</h2>
    <p class="specialty">Footwear Fitting Specialist</p>
    <ul class="contact contact--direct">
      <li>
        <svg class="icon" viewBox="0 0 24 24" aria-hidden="true"><path d="M6.6 10.8a15 15 0 0 0 6.6 6.6l2.2-2.2a1 1 0 0 1 1-.25 11.4 11.4 0 0 0 3.6.57 1 1 0 0 1 1 1V20a1 1 0 0 1-1 1A17 17 0 0 1 3 4a1 1 0 0 1 1-1h3.5a1 1 0 0 1 1 1c0 1.25.2 2.45.57 3.57a1 1 0 0 1-.25 1z"/></svg>
        <span>9187 2630</span>
      </li>
      <li>
        <svg class="icon" viewBox="0 0 24 24" aria-hidden="true"><path d="M2 5h20v14H2z"/><path d="M3 6l9 6.3L21 6" fill="none" stroke="var(--purple)" stroke-width="2"/></svg>
        <span>darnellshoes218@examplemail.com</span>
      </li>
    </ul>
    <ul class="contact contact--address">
      <li>
        <svg class="icon" viewBox="0 0 24 24" aria-hidden="true"><path d="M12 2a7 7 0 0 0-7 7c0 5 7 13 7 13s7-8 7-13a7 7 0 0 0-7-7zm0 9.5a2.5 2.5 0 1 1 0-5 2.5 2.5 0 0 1 0 5z"/></svg>
        <span>218 Quarry St, Fernleigh Downs 3187</span>
      </li>
      <li class="indent">(cnr. Hartwick Rd and Quarry St)</li>
    </ul>
  </section>
</main>
</body>
</html>
```